Harbor Advance, Inc.

We need a website design for a new company based in Orange County, CA but will be serving client's throughout all of California. We provide non-recourse loans/ pre-litigation funding for client's in personal injury and employment cases. Generally, if a client has an active case and they need money for cost of living, the client will contact a company like ours to provide a loan. We would like to see designs that are sleek, simple and easy to use. The final design should communicate trustworthiness, financial safety and promptness.

Hi, I like KW's designs. I am having him work on a hybrid of two of his designs. We had a little miscommunication, but we are almost there. Best, Ned

```html
<!DOCTYPE html>
<html lang="en">
<head>
<meta charset="utf-8">
<title>Harbor Advance, Inc.</title>
<link href="https://fonts.googleapis.com/css2?family=Tinos:wght@400;700&family=Lato:wght@400;700&family=Jost:wght@400;500&display=swap" rel="stylesheet">
<style>
:root{
  --teal:#0f3b40;
  --orange:#c8620d;
  --orange-soft:#d9822f;
  --ink:#1c1c1c;
  --muted:#8a8a8a;
  --dark:#2b2b2b;
  --white:#ffffff;
  --line:#d5d5d5;
}
*{margin:0;padding:0;box-sizing:border-box}
html,body{width:1200px;height:3536px;overflow:hidden}
body{position:relative;font-family:"Lato",Arial,sans-serif;color:var(--ink);background:var(--white)}
.abs{position:absolute}
.serif{font-family:"Tinos","Times New Roman",serif}
.jost{font-family:"Jost","Futura",sans-serif}

/* top bar */
.topbar{left:0;top:0;width:1200px;height:52px;background:var(--teal)}
.social-box{position:absolute;top:12px;width:28px;height:28px;background:var(--orange)}
.topbar .contact{position:absolute;top:0;height:52px;display:flex;align-items:center;gap:12px;color:var(--white);font-size:15px}

/* nav */
.nav{left:0;top:52px;width:1200px;height:104px;background:var(--white)}
.brand{position:absolute;left:78px;top:31px;display:flex;align-items:center;gap:14px}
.brand-mark{width:42px;height:42px;border-radius:50%;background:var(--orange)}
.brand-name{font-family:"Tinos",serif;font-weight:700;font-size:26px;color:var(--teal);letter-spacing:.5px}
.menu a{position:absolute;top:46px;font-size:14px;color:var(--ink);text-decoration:none;letter-spacing:.5px}
.menu a.active{color:var(--orange);font-weight:700}
.menu-caret{position:absolute;left:589px;top:70px}
.search{position:absolute;left:1070px;top:26px;width:52px;height:52px;border:1px solid var(--line);border-radius:50%}

/* hero */
.hero{left:0;top:156px;width:1200px;height:575px;background:linear-gradient(100deg,#5b4a3e 0%,#8a7d72 35%,#b6b2ae 60%,#6e6a67 80%,#3c3a38 100%)}
.hero-frame{position:absolute;left:125px;top:115px;width:594px;height:349px;border:1px solid rgba(255,255,255,.7)}
.hero-panel{position:absolute;left:141px;top:134px;width:542px;height:323px;background:rgba(200,98,13,.88)}
.hero h1{position:absolute;left:43px;top:62px;font-family:"Tinos",serif;font-weight:700;font-size:38px;color:#3a2a12;letter-spacing:1px}
.hero p{position:absolute;left:43px;top:122px;width:470px;font-size:14px;line-height:23px;color:var(--white)}
.btn{position:absolute;display:flex;align-items:center;justify-content:center;font-size:15px;letter-spacing:.5px;text-transform:uppercase}
.btn-teal{background:var(--teal);color:var(--white);border:2px solid var(--white)}
.btn-ghost{color:var(--white);border:2px solid var(--white)}

/* about */
.about{left:0;top:731px;width:1200px;height:594px}
.about-photo{position:absolute;left:92px;top:61px;width:519px;height:469px;background:linear-gradient(120deg,#4a3a30,#8c7d70 55%,#c8c2bb)}
.about-card{position:absolute;left:561px;top:113px;width:540px;height:365px;background:var(--white);box-shadow:0 4px 18px rgba(0,0,0,.18)}
.about-card h2{position:absolute;left:44px;top:42px;font-family:"Tinos",serif;font-weight:700;font-size:33px}
.divider{position:absolute;height:10px}
.divider::before,.divider::after{content:"";position:absolute;top:4px;width:78px;height:1px;background:var(--line)}
.divider::before{left:0}.divider::after{right:0}
.divider span{position:absolute;left:50%;top:0;width:10px;height:10px;margin-left:-5px;border-radius:50%;background:var(--muted)}
.about-card p{position:absolute;left:44px;top:120px;width:460px;font-size:13px;line-height:24px;color:var(--muted)}
.btn-orange{background:var(--orange);color:var(--ink);border:2px solid var(--teal)}

/* services */
.services{left:0;top:1325px;width:1200px;height:813px;background:linear-gradient(90deg,#3a3330 0%,#262322 45%,#2e2926 70%,#4a3d35 100%)}
.section-title{position:absolute;left:0;width:1200px;text-align:center;font-family:"Tinos",serif;font-weight:700;font-size:35px}
.section-lead{position:absolute;left:290px;width:620px;text-align:center;font-size:13px;line-height:25px}
.service-card{position:absolute;top:262px;width:415px;height:478px;background:var(--white);text-align:center}
.icon-ring{position:absolute;left:152px;top:38px;width:112px;height:112px;border-radius:50%;border:3px solid #f0d3b6;background:var(--orange)}
.service-card h3{position:absolute;left:0;top:184px;width:415px;font-family:"Jost",sans-serif;font-weight:400;font-size:27px;color:var(--ink)}
.service-card p{position:absolute;left:50px;top:237px;width:315px;font-size:13px;line-height:24px;color:var(--muted)}
.btn-teal-o{background:var(--teal);color:var(--white);border:3px solid var(--orange)}

/* news */
.news{left:0;top:2138px;width:1200px;height:875px}
.news-card{position:absolute;top:262px;width:323px}
.news-photo{position:absolute;left:0;top:23px;width:313px;height:210px}
.news-shadow{position:absolute;left:10px;top:33px;width:313px;height:210px;background:var(--orange)}
.news-date{position:absolute;left:57px;top:0;width:207px;height:47px;background:var(--teal);color:var(--white);font-size:15px;display:flex;align-items:center;justify-content:center}
.news-card h3{position:absolute;left:0;top:282px;font-family:"Jost",sans-serif;font-weight:400;font-size:22px}
.news-meta{position:absolute;left:0;top:335px;font-size:13px;color:var(--muted);white-space:nowrap}
.news-meta b{color:var(--ink);font-weight:700}
.news-card p{position:absolute;left:0;top:364px;width:320px;font-size:13px;line-height:24px;color:var(--muted)}
.btn-line{border:2px solid var(--teal);color:var(--teal);background:var(--white)}

/* footer */
.footer{left:0;top:3013px;width:1200px;height:523px}
.footer-bg{position:absolute;left:0;top:64px;width:1200px;height:389px;background:linear-gradient(180deg,#2b2b2b,#1e1e1e)}
.contact-bar{position:absolute;left:78px;top:0;width:1044px;height:123px;background:var(--orange)}
.outline-box{position:absolute;top:33px;width:52px;height:52px;border:2px solid var(--white)}
.contact-item{position:absolute;top:34px;display:flex;gap:14px;align-items:center;color:var(--white)}
.contact-item small{display:block;font-size:14px}
.contact-item strong{display:block;font-size:18px;font-weight:700}
.footer h4{position:absolute;top:190px;font-family:"Tinos",serif;font-weight:700;font-size:21px;color:var(--white)}
.footer-brand{position:absolute;left:78px;top:190px;display:flex;align-items:center;gap:8px}
.footer-brand i{width:26px;height:26px;border-radius:50%;background:var(--white);display:block}
.footer-brand span{font-family:"Tinos",serif;font-weight:700;font-size:17px;color:var(--white)}
.footer p.f-text{position:absolute;top:238px;font-size:13px;line-height:25px;color:#e6e6e6}
.f-list{position:absolute;top:240px;list-style:none;font-size:13px;color:#e6e6e6;line-height:29px}
.f-list li::before{content:"- ";}
.subscribe{position:absolute;left:884px;top:306px;width:236px;height:47px;border:1px solid #bbb;background:#151515}
.subscribe span{position:absolute;left:12px;top:14px;font-size:13px;color:#e6e6e6}
.subscribe i{position:absolute;right:4px;top:4px;width:40px;height:37px;background:var(--orange)}
.copyright{position:absolute;left:0;top:453px;width:1200px;height:70px;background:var(--orange);color:var(--white);font-size:13px;display:flex;align-items:center;justify-content:center}
</style>
</head>
<body>

<header class="abs topbar">
  <span class="social-box" style="left:80px" aria-label="LinkedIn"></span>
  <span class="social-box" style="left:117px" aria-label="Twitter"></span>
  <span class="social-box" style="left:154px" aria-label="Facebook"></span>
  <div class="contact" style="left:735px">
    <svg width="20" height="14" viewBox="0 0 20 14"><rect x="1" y="1" width="18" height="12" fill="none" stroke="#c8620d" stroke-width="2"/><path d="M1 1l9 7 9-7" fill="none" stroke="#c8620d" stroke-width="2"/></svg>
    hello@harboradvance.com
  </div>
  <div class="contact" style="left:1000px">
    <svg width="14" height="18" viewBox="0 0 14 18"><rect x="1" y="1" width="12" height="16" rx="2" fill="none" stroke="#c8620d" stroke-width="2"/><circle cx="7" cy="14" r="1.3" fill="#c8620d"/></svg>
    (100) 555 0142
  </div>
</header>

<nav class="abs nav">
  <div class="brand"><span class="brand-mark"></span><span class="brand-name">HARBOR ADVANCE, INC.</span></div>
  <div class="menu">
    <a class="active" href="#" style="left:578px">HOME</a>
    <a href="#" style="left:665px">ABOUT</a>
    <a href="#" style="left:758px">SERVICES</a>
    <a href="#" style="left:869px">NEWS</a>
    <a href="#" style="left:954px">CONTACT</a>
  </div>
  <svg class="menu-caret" width="18" height="14" viewBox="0 0 18 14"><path d="M9 0l9 14H0z" fill="#c8620d"/></svg>
  <div class="search">
    <svg width="52" height="52" viewBox="0 0 52 52"><circle cx="24" cy="24" r="7" fill="none" stroke="#555" stroke-width="2"/><path d="M29 29l6 6" stroke="#555" stroke-width="2"/></svg>
  </div>
</nav>

<section class="abs hero" role="img" aria-label="Smiling business advisor holding a tablet in a busy office">
  <div class="hero-frame"></div>
  <div class="hero-panel">
    <h1>LOREM IPSUM SIMPLY</h1>
    <p>Lorem ipsum dolor sit amet, consectetur adipiscing elit, sed do eiusmod tempor incididunt ut labore et dolore magna aliqua. Ut enim ad minim veniam, quis nostrud exercitation ullamco laboris commodo consequat.</p>
    <span class="btn btn-teal" style="left:41px;top:215px;width:143px;height:54px">Contact Us</span>
    <span class="btn btn-ghost" style="left:201px;top:215px;width:148px;height:54px">Learn More</span>
  </div>
</section>

<section class="abs about">
  <div class="about-photo" role="img" aria-label="Advisor shaking hands with a client across a desk"></div>
  <div class="about-card">
    <h2>About Harbor Advance, Inc.</h2>
    <div class="divider" style="left:153px;top:94px;width:190px"><span></span></div>
    <p>Lorem ipsum dolor sit amet, consectetur adipiscing elit, sed do eiusmod tempor incididunt ut labore et dolore magna aliqua. Ut enim ad minim veniam, quis nostrud exercitation ullamco laboris nisi ut aliquip ex ea commodo consequat. Duis aute irure dolor in reprehenderit in voluptate velit esse cillum dolore eu fugiat nulla pariatur.</p>
    <span class="btn btn-orange" style="left:41px;top:272px;width:148px;height:54px">Read More</span>
  </div>
</section>

<section class="abs services" role="img" aria-label="Dim courtroom backdrop with scales of justice and gavel">
  <h2 class="section-title" style="top:60px;color:var(--white)">Harbor Advance Services</h2>
  <div class="divider" style="left:505px;top:113px;width:190px"><span style="background:var(--white)"></span></div>
  <p class="section-lead" style="top:140px;color:var(--white);font-weight:700">Lorem ipsum dolor sit amet, consectetur adipiscing elit, sed do eiusmod tempor incididunt ut labore et dolore magna aliqua. Ut enim ad minim veniam, quis nostrud exercitation ullamco laboris commodo consequat.</p>

  <article class="service-card" style="left:158px">
    <div class="icon-ring">
      <svg width="106" height="106" viewBox="0 0 106 106"><path d="M34 70h38M38 68V50M46 68V42M54 68V54" stroke="#fff" stroke-width="3" fill="none"/><circle cx="64" cy="46" r="9" fill="none" stroke="#fff" stroke-width="3"/></svg>
    </div>
    <h3>Non-recourse loans</h3>
    <p>Lorem ipsum dolor sit amet, consectetur adipiscing elit, sed do eiusmod tempor incididunt ut labore et dolore magna aliqua. Ut enim ad minim veniam, quis nostrud exercitation ullamco laboris nisi ut aliquip ex ea commodo consequat.</p>
    <span class="btn btn-teal-o" style="left:134px;top:385px;width:148px;height:54px">Read More</span>
  </article>

  <article class="service-card" style="left:627px">
    <div class="icon-ring">
      <svg width="106" height="106" viewBox="0 0 106 106"><path d="M53 36v34M40 70h26M34 44h38" stroke="#fff" stroke-width="3" fill="none"/><path d="M34 44l-6 12h12zM72 44l-6 12h12z" fill="none" stroke="#fff" stroke-width="2.5"/></svg>
    </div>
    <h3>Pre-litigation funding</h3>
    <p>Lorem ipsum dolor sit amet, consectetur adipiscing elit, sed do eiusmod tempor incididunt ut labore et dolore magna aliqua. Ut enim ad minim veniam, quis nostrud exercitation ullamco laboris nisi ut aliquip ex ea commodo consequat.</p>
    <span class="btn btn-teal-o" style="left:134px;top:385px;width:148px;height:54px">Read More</span>
  </article>
</section>

<section class="abs news">
  <h2 class="section-title" style="top:60px">News Updates</h2>
  <div class="divider" style="left:505px;top:113px;width:190px"><span></span></div>
  <p class="section-lead" style="top:140px;color:var(--muted)">Lorem ipsum dolor sit amet, consectetur adipiscing elit, sed do eiusmod tempor incididunt ut labore et dolore magna aliqua. Ut enim ad minim veniam, quis nostrud exercitation ullamco laboris commodo consequat.</p>

  <article class="news-card" style="left:78px">
    <div class="news-shadow"></div>
    <div class="news-photo" role="img" aria-label="Professional working on a laptop in a bright office" style="background:linear-gradient(135deg,#d9d2c8,#8a7a6a)"></div>
    <div class="news-date">3RD, JANUARY 2019</div>
    <h3>Case Investigation</h3>
    <div class="news-meta">by <b>Marcus Hale</b> &nbsp;/&nbsp; <b>lawyer</b> &nbsp;/&nbsp; 5 comments</div>
    <p>Lorem Ipsum is simply dummy text of the print printing and typesetting industry. Lorem Ipsum has been the industry's standard dummy text ever since the 1500s.</p>
    <span class="btn btn-line" style="left:0;top:482px;width:148px;height:54px">Read More</span>
  </article>

  <article class="news-card" style="left:438px">
    <div class="news-shadow"></div>
    <div class="news-photo" role="img" aria-label="Team meeting around a conference table" style="background:linear-gradient(135deg,#e4e4e4,#6f7478)"></div>
    <div class="news-date">3RD, JANUARY 2019</div>
    <h3>Case Investigation</h3>
    <div class="news-meta">by <b>Marcus Hale</b> &nbsp;/&nbsp; <b>lawyer</b> &nbsp;/&nbsp; 5 comments</div>
    <p>Lorem Ipsum is simply dummy text of the print printing and typesetting industry. Lorem Ipsum has been the industry's standard dummy text ever since the 1500s.</p>
    <span class="btn btn-line" style="left:0;top:482px;width:148px;height:54px">Read More</span>
  </article>

  <article class="news-card" style="left:799px">
    <div class="news-shadow"></div>
    <div class="news-photo" role="img" aria-label="Overhead view of colleagues reviewing documents" style="background:linear-gradient(135deg,#eef0f0,#7d8c90)"></div>
    <div class="news-date">3RD, JANUARY 2019</div>
    <h3>Case Investigation</h3>
    <div class="news-meta">by <b>Marcus Hale</b> &nbsp;/&nbsp; <b>lawyer</b> &nbsp;/&nbsp; 5 comments</div>
    <p>Lorem Ipsum is simply dummy text of the print printing and typesetting industry. Lorem Ipsum has been the industry's standard dummy text ever since the 1500s.</p>
    <span class="btn btn-line" style="left:0;top:482px;width:148px;height:54px">Read More</span>
  </article>
</section>

<footer class="abs footer">
  <div class="footer-bg" role="img" aria-label="Darkened courthouse columns"></div>
  <div class="contact-bar">
    <span class="outline-box" style="left:30px" aria-label="LinkedIn"></span>
    <span class="outline-box" style="left:94px" aria-label="Twitter"></span>
    <span class="outline-box" style="left:158px" aria-label="Facebook"></span>
    <div class="contact-item" style="left:390px">
      <svg width="54" height="40" viewBox="0 0 54 40"><rect x="2" y="2" width="50" height="36" fill="#0f3b40"/><path d="M2 2l25 20 25-20" fill="none" stroke="#c8620d" stroke-width="3"/></svg>
      <div><small>Email</small><strong>hello@harboradvance.com</strong></div>
    </div>
    <div class="contact-item" style="left:702px">
      <svg width="30" height="52" viewBox="0 0 30 52"><rect x="2" y="2" width="26" height="48" rx="4" fill="none" stroke="#0f3b40" stroke-width="3"/><circle cx="15" cy="42" r="3" fill="#0f3b40"/></svg>
      <div><small>Phone</small><strong>(100) 555 0142</strong></div>
    </div>
  </div>

  <div class="footer-brand"><i></i><span>HARBOR ADVANCE, INC.</span></div>
  <p class="f-text" style="left:78px;width:245px">Lorem Ipsum is simply dummy text of the print printing and typesetting industry. Lorem Ipsum has been...</p>

  <h4 style="left:401px">Quick Links</h4>
  <ul class="f-list" style="left:412px"><li>Home</li><li>About</li><li>Services</li><li>News</li><li>Contact</li></ul>

  <h4 style="left:615px">Services</h4>
  <ul class="f-list" style="left:615px"><li>Non-recourse loans</li><li>Pre-litigation funding</li></ul>

  <h4 style="left:884px">Get In Touch</h4>
  <p class="f-text" style="left:884px;width:240px">Lorem Ipsum is simply dummy text of the print printing and typesetting.</p>
  <div class="subscribe"><span>Enter Email...</span><i><svg width="40" height="37" viewBox="0 0 40 37"><path d="M11 19l18-8-6 17-4-6z" fill="#fff"/></svg></i></div>

  <div class="copyright">Copyright © HARBOR ADVANCE, Inc - 2018 . All Right Reserved</div>
</footer>

</body>
</html>
```